Plant Grower/Nursery needs a fun, professional and fresh 1/2 page print ad for a high profile gar...

We need a print ad for a garden tour geared towards plant enthusiasts that support California Native, natural and sustainable plants. A good percentage of our target market want a conservation and earth friendly approach to gardens/landscaping. We want to target this market, as well as, people who are looking for a pretty/colorful landscape that require little water/maintenance. **PLEASE LET US KNOW IF YOU HAVE QUESTIONS OR NEED MORE INFORMATION. WE ALSO HAVE MANY MORE PICTURES IF THESE DON'T WORK FOR YOUR DESIGN. ***THE AD CAN HAVE AS FEW AS 1 PHOTO - WE ARE POSTING SEVERAL IN HOPES THAT YOU CAN FIND WHAT IS PERFECT FOR YOUR IDEA!!Thank you

Target Market(s)

Gardeners, Landscapers, Landscape Designers/Architects, Cities and Municipalities.

Industry/Entity Type

Agriculture

Font styles to use
Serif
Sans Serif

Colors

Designer to choose colors to be used in the design.

Requirements
Must have
• We believe in growing regionally appropriate plants for Southern California that beatify our natural and urban landscapes.
• For over 20 years, our owners and staff take pride in providing timely, expert, and honest service.
Nice to have
• At least 1 photo. Eye catchy with a modern earthy feel.
• Hundreds of species/hybrids in stock of California Natives, Succulents, Ornamental Grasses, Standard Stock Items and Unique Plants.

```html
<!DOCTYPE html>
<html lang="en">
<head>
<meta charset="utf-8">
<title>Native Plant Nursery Ad</title>
<link rel="stylesheet" href="https://fonts.googleapis.com/css2?family=Roboto:wght@400;500&display=swap">
<style>
  :root {
    --backdrop: #6f6f6f;
    --forest: #0b6212;
    --cream: #ffffd4;
    --pill: #2a2a2a;
    --white: #ffffff;
    --veil: rgba(40, 40, 40, 0.55);
  }
  * { margin: 0; padding: 0; box-sizing: border-box; }
  html, body { width: 1200px; height: 1200px; overflow: hidden; }
  body {
    background: var(--backdrop);
    font-family: "Roboto", Arial, sans-serif;
    position: relative;
  }
  .ad {
    position: absolute;
    left: 105px; top: 247px;
    width: 990px; height: 706px;
    background: var(--cream);
    overflow: hidden;
  }
  .hero {
    position: absolute; left: 0; top: 0;
    width: 990px; height: 405px;
    background:
      radial-gradient(ellipse 120px 70px at 80px 60px, #f0521f 0%, rgba(240,82,31,0) 100%),
      radial-gradient(ellipse 200px 60px at 500px 370px, #f4621c 0%, rgba(244,98,28,0) 100%),
      radial-gradient(ellipse 110px 50px at 100px 380px, #ef5a1e 0%, rgba(239,90,30,0) 100%),
      radial-gradient(ellipse 90px 110px at 700px 200px, #e2481a 0%, rgba(226,72,26,0) 100%),
      radial-gradient(ellipse 260px 150px at 800px 80px, #8a6a4a 0%, rgba(138,106,74,0) 100%),
      radial-gradient(ellipse 220px 180px at 950px 320px, #8d7454 0%, rgba(141,116,84,0) 100%),
      linear-gradient(135deg, #6f9a6a 0%, #8fb48a 35%, #5e7d55 65%, #7c9870 100%);
  }
  .mission {
    position: absolute;
    left: 31px; top: 146px;
    width: 925px; height: 164px;
    background: var(--veil);
    display: flex; align-items: center; justify-content: center;
    text-align: center;
    color: var(--white);
    font-size: 30px; line-height: 36px; font-weight: 400;
    padding-left: 20px;
  }
  .service-band {
    position: absolute; left: 0; top: 405px;
    width: 990px; height: 58px;
    background: var(--forest);
    color: var(--white);
    font-size: 20px;
    display: flex; align-items: center; justify-content: center;
  }
  .gallery-photo {
    position: absolute; top: 478px;
    width: 266px; height: 153px;
    border: 4px solid var(--forest);
    border-radius: 20px;
  }
  .photo-leaves { left: 49px; background: linear-gradient(135deg, #3f8a33, #5aa844 50%, #2f6a28); }
  .photo-yarrow { left: 353px; background: radial-gradient(ellipse at 55% 45%, #eeeee6 0%, #c9cfc0 40%, #2a3a22 85%); }
  .photo-monkeyflower { left: 666px; background: radial-gradient(ellipse at 30% 50%, #e8208e 0%, rgba(232,32,142,0) 45%), radial-gradient(ellipse at 75% 55%, #e8208e 0%, rgba(232,32,142,0) 45%), linear-gradient(135deg, #6b5a6a, #5a6a4a); }
  .footer-rule {
    position: absolute; left: 0; top: 674px;
    width: 990px; height: 7px;
    background: var(--forest);
  }
  .website {
    position: absolute; left: 254px; top: 658px;
    width: 454px; height: 34px;
    background: var(--pill);
    border-radius: 17px;
    color: var(--white);
    font-size: 24px; font-weight: 500;
    display: flex; align-items: center; justify-content: center;
  }
</style>
</head>
<body>
  <div class="ad">
    <div class="hero" role="img" aria-label="Close-up photo of orange tubular wildflowers among fuzzy grey-green leaves"></div>
    <p class="mission">We believe in growing regionally appropriate plants for<br>Southern California that beatify our natural and urban landscapes.</p>
    <p class="service-band">For over 20 years, our owners and staff take pride in providing timely, expert, and honest service.</p>
    <div class="gallery-photo photo-leaves" role="img" aria-label="Photo of green serrated strawberry-like leaves"></div>
    <div class="gallery-photo photo-yarrow" role="img" aria-label="Photo of white yarrow flower clusters"></div>
    <div class="gallery-photo photo-monkeyflower" role="img" aria-label="Photo of two magenta monkeyflower blooms"></div>
    <div class="footer-rule"></div>
    <p class="website">www.yourwebsite.com</p>
  </div>
</body>
</html>
```